Growing Wellness Company Needs an Amazing Cover for a series of Booklets

We are publishing our own series of booklets on health & wellness topics, called Vital Spark Primers and need an inspiring, modern design for the cover. We are beginning with the Title Diabetes: Type 2, but we will use this design for other titles later one.

SIZE:
This will be the front and back of a 8.5 x 5.5 booklet, plus 2 sample interior pages.

COLOR:
We are an industry leaders and prefer touse vibrant colors and designs to inspire our clients to change to a healthier lifestyle.

REQUIREMENTS:
I am attaching our Vital Spark logo, which needs to be on each cover, but does not need to be the focal point. You may you the words vital spark or just the Vital Spark. The topic/title needs to be no lower than 1/2" from the top of the cover.

I'm attaching some samples of items I like, but please be creative!
If you would like to see some of our other in-house samples of publications send me a message and I'll show you. I will give detailed feedback so dive in and get creative!
Updates

FRONT COVER: 
1. Can you please make sure the title is in the top 1.5" of the page, i can't tell from this view. 
Type 2 Diabetes (1st line, bigger) 
A Simple Guide to Understanding & Controlling Your Blood Sugar (Second Row, much smaller) this can also be below the 1.5" line if it needs to be. 
3.We would like to see three shapes maybe toward the bottom with these words in them, one word per shape. inspire, equip, succeed 

IMAGE 
1. We would like you to leave a placeholder for an image, but would like to see different shapes, such as a rounded square or rectangle or a rectangle with two square corners and two rounded corners. 
2. Please play with some different border options as well,

BACKSIDE 
1. please put our information on the back side on the bottom, small. the information i will put in a file on the brief, the 2nd page has our address, phone, etc. 
2. Add our MC logo (attached as an image in the design brief)

Thanks! looking forward to what else you have. 

Reason: I want to give more time to get more/better designs in, i know this is a little more involved project.

Reason: Still not happy with designs, would like to see more.

Hello - thank you for submitting designs, the designs are getting a little too busy....here is a website I love the simplicity of...thanks!  http://www.brindlevalecare.example   

Reason: We are getting closer to narrowing it down, I want to give the designers a few more days to tweak their designs, then i will ask the final 2 or 3 to submit a couple version of the inside pages. I will supply text for those so you know what you're working with. Thanks!

Target Market(s)

Our clients are adults, about 50/50 men & women in the age range from 20-70 with most being in their early 50's. from high school education up to professional degrees

Industry/Entity Type

Industry

Font styles to use
Serif
Sans Serif
Script

Colors
a64599
e34197
00a98f
9bcb3c
ffc214
f78f20
f37122
0492cd
6a439a

Requirements
Must have
• Eye catching, inspiring design that entices people to read our booklet:

I need a front and back cover and 2 interior page samples , we will be using more of an info graphic style inside possible with a few actual photographs

FRONT COVER REQUIREMENTS:
Title (must be no lower than 1.5" below the top)
Vital Spark Logo (attached in pink and green)
Meadowcrest Wellness' Logo

BACK COVER REQUIREMENTS:
a place for summary text
meadowcrest wellness contact information
a place for an item # (can be small, no barcode)
Nice to have
• the colors i chose are samples, does not need to include every color, each title we write will have a different color story

I can appreciate a white cover with some amazing art of pops of color, but i would also love a really rich color with subtle tone on tone things (see the navy blue cover picture)
Should not have
• boring colors, lots of pictures, typical booklet design

```html
<!DOCTYPE html>
<html lang="en">
<head>
<meta charset="utf-8">
<title>Vital Spark Primers – Type 2 Diabetes Covers</title>
<link rel="stylesheet" href="https://fonts.googleapis.com/css2?family=Questrial&family=Inter:wght@800&family=Playfair+Display:wght@900&family=Courgette&family=Montserrat:wght@700&display=swap">
<style>
  :root {
    --paper: #ffffff;
    --leaf-green: #8bc043;
    --petal-green: #9bcb4c;
    --petal-teal: #155a78;
    --petal-pink: #e23a96;
    --petal-orange: #f69033;
    --frame-grey: #818285;
    --title-ink: #3a3a3c;
    --subtitle-ink: #1d5c70;
    --label-ink: #111111;
  }
  * { margin: 0; padding: 0; box-sizing: border-box; }
  html, body { width: 1200px; height: 942px; overflow: hidden; background: var(--paper); }
  body { position: relative; font-family: "Questrial", sans-serif; }

  .spread-label {
    position: absolute; top: 20px; width: 533px; text-align: center;
    font-family: "Questrial", sans-serif; font-size: 24px; color: var(--label-ink);
    letter-spacing: 0.5px;
  }
  .spread-label--back { left: 55px; }
  .spread-label--front { left: 605px; }

  .cover {
    position: absolute; top: 62px; width: 533px; height: 823px; overflow: hidden;
    background: linear-gradient(to bottom, #ffffff 0%, #d7e9bd 15%, #a9d06f 25%, var(--leaf-green) 31%, var(--leaf-green) 100%);
  }
  .cover--back { left: 55px; }
  .cover--front { left: 605px; }
  .cover svg.flower { position: absolute; left: 0; top: 0; }

  .summary text { font-family: "Questrial", sans-serif; font-size: 13.4px; fill: #ffffff; }

  .publisher {
    position: absolute; left: 8px; top: 766px; display: flex; align-items: flex-start; gap: 6px;
    color: #ffffff;
  }
  .publisher__mark { width: 38px; height: 38px; border: 3px solid #ffffff; border-radius: 4px; margin-top: 2px; flex: none; }
  .publisher__name { font-size: 6.8px; font-weight: 700; line-height: 10px; white-space: nowrap; }
  .publisher__line { font-size: 5.6px; line-height: 7px; white-space: nowrap; }
  .publisher__line--strong { font-weight: 700; }

  .item-number {
    position: absolute; left: 425px; top: 805px; font-size: 7px; color: #ffffff; letter-spacing: 0.3px;
  }

  .series-mark {
    position: absolute; left: 14px; top: 783px; display: flex; align-items: center; gap: 6px;
    color: #ffffff; font-size: 13px;
  }
  .series-mark__dot { width: 18px; height: 18px; border-radius: 50%; background: #ffffff; }
</style>
</head>
<body>

<div class="spread-label spread-label--back">BACK COVER</div>
<div class="spread-label spread-label--front">FRONT COVER</div>

<!-- Back cover -->
<section class="cover cover--back">
  <svg class="flower" width="533" height="823" viewBox="0 0 533 823">
    <g fill="none" stroke-linejoin="round">
      <g stroke="#ffffff" stroke-width="96">
        <path d="M358 650 H150 A150 150 0 0 1 0 500 V470 A180 180 0 0 1 180 290 A178 178 0 0 1 358 468 Z"/>
        <path d="M368 650 V568 A82 82 0 0 1 450 486 A82 82 0 0 1 532 568 A82 82 0 0 1 450 650 Z"/>
        <path d="M358 658 V740 A82 82 0 0 1 276 822 A82 82 0 0 1 195 740 A82 82 0 0 1 277 658 Z"/>
        <path d="M368 658 H450 A82 82 0 0 1 532 740 A82 82 0 0 1 450 822 A82 82 0 0 1 368 740 Z"/>
      </g>
      <g stroke="var(--frame-grey)" stroke-width="52">
        <path d="M358 650 H150 A150 150 0 0 1 0 500 V470 A180 180 0 0 1 180 290 A178 178 0 0 1 358 468 Z"/>
        <path d="M368 650 V568 A82 82 0 0 1 450 486 A82 82 0 0 1 532 568 A82 82 0 0 1 450 650 Z"/>
        <path d="M358 658 V740 A82 82 0 0 1 276 822 A82 82 0 0 1 195 740 A82 82 0 0 1 277 658 Z"/>
        <path d="M368 658 H450 A82 82 0 0 1 532 740 A82 82 0 0 1 450 822 A82 82 0 0 1 368 740 Z"/>
      </g>
    </g>
    <path fill="var(--petal-orange)" d="M358 650 H150 A150 150 0 0 1 0 500 V470 A180 180 0 0 1 180 290 A178 178 0 0 1 358 468 Z"/>
    <path fill="var(--petal-green)" d="M368 650 V568 A82 82 0 0 1 450 486 A82 82 0 0 1 532 568 A82 82 0 0 1 450 650 Z"/>
    <path fill="var(--petal-teal)" d="M358 658 V740 A82 82 0 0 1 276 822 A82 82 0 0 1 195 740 A82 82 0 0 1 277 658 Z"/>
    <path fill="var(--petal-pink)" d="M368 658 H450 A82 82 0 0 1 532 740 A82 82 0 0 1 450 822 A82 82 0 0 1 368 740 Z"/>

    <g class="summary">
      <text x="103" y="327" textLength="164" lengthAdjust="spacingAndGlyphs">Lorem ipsum dolor sit</text>
      <text x="95" y="344" textLength="170" lengthAdjust="spacingAndGlyphs">amet, consectetur adipiscing</text>
      <text x="55" y="361" textLength="238" lengthAdjust="spacingAndGlyphs">elit. Vivamus tortor diam, lobortis sed</text>
      <text x="45" y="378" textLength="251" lengthAdjust="spacingAndGlyphs">tellus vitae, ultricies pulvinar ligula. Cras</text>
      <text x="33" y="394" textLength="269" lengthAdjust="spacingAndGlyphs">faucibus consectetur sollicitudin. Morbi</text>
      <text x="27" y="410" textLength="285" lengthAdjust="spacingAndGlyphs">lorem eros, malesuada faucibus venenatis</text>
      <text x="20" y="426" textLength="299" lengthAdjust="spacingAndGlyphs">non, cursus nec orci. Vestibulum consequat</text>
      <text x="17" y="441" textLength="292" lengthAdjust="spacingAndGlyphs">dolor ac sem ultrices sollicitudin. Pellentesque</text>
      <text x="11" y="458" textLength="298" lengthAdjust="spacingAndGlyphs">suscipit dignissim tortor, non semper turpis</text>
      <text x="7" y="474" textLength="79" lengthAdjust="spacingAndGlyphs">bibendum at.</text>
      <text x="58" y="490" textLength="259" lengthAdjust="spacingAndGlyphs">Donec ac est at neque auctor convallis.</text>
      <text x="17" y="506" textLength="325" lengthAdjust="spacingAndGlyphs">Cras egestas elit et urna euismod, quis luctus dolor</text>
      <text x="25" y="522" textLength="269" lengthAdjust="spacingAndGlyphs">consequat. Vestibulum scelerisque neque.</text>
      <text x="41" y="539" textLength="296" lengthAdjust="spacingAndGlyphs">Lorem ipsum dolor sit amet, consectetur</text>
      <text x="35" y="554" textLength="307" lengthAdjust="spacingAndGlyphs">adipiscing elit. Vivamus tortor diam, lobortis sed</text>
      <text x="47" y="570" textLength="253" lengthAdjust="spacingAndGlyphs">tellus vitae, ultricies pulvinar ligula. Cras</text>
      <text x="61" y="587" textLength="245" lengthAdjust="spacingAndGlyphs">faucibus consectetur sollicitudin. Morbi</text>
      <text x="50" y="603" textLength="239" lengthAdjust="spacingAndGlyphs">lorem eros, malesuada faucibus</text>
      <text x="110" y="619" textLength="197" lengthAdjust="spacingAndGlyphs">venenatis non, cursus nec orci.</text>
    </g>
  </svg>

  <div class="publisher">
    <div class="publisher__mark"></div>
    <div>
      <div class="publisher__name">Meadowcrest Wellness LLC</div>
      <div class="publisher__line">42 Orchard Lane</div>
      <div class="publisher__line">P.O. Box 210</div>
      <div class="publisher__line">Fairmont, NE 68000</div>
      <div class="publisher__line publisher__line--strong">meadowcrest-wellness.example</div>
      <div class="publisher__line publisher__line--strong">555.014.2290</div>
    </div>
  </div>

  <div class="item-number">1234092193819</div>
</section>

<!-- Front cover -->
<section class="cover cover--front">
  <svg class="flower" width="533" height="823" viewBox="0 0 533 823">
    <defs>
      <linearGradient id="photo-tone" x1="0" y1="0" x2="1" y2="1">
        <stop offset="0" stop-color="#cfe0d2"/>
        <stop offset="0.35" stop-color="#e9d3bd"/>
        <stop offset="0.7" stop-color="#f3ede6"/>
        <stop offset="1" stop-color="#dcdcdc"/>
      </linearGradient>
    </defs>

    <g class="title-block">
      <text x="32" y="88" textLength="471" lengthAdjust="spacingAndGlyphs"
            font-family="Inter, sans-serif" font-weight="800" font-size="68" letter-spacing="-3" fill="var(--title-ink)">Type<tspan dx="8" font-family="'Playfair Display', serif" font-weight="900" fill="var(--petal-pink)">2</tspan><tspan dx="8">Diabetes</tspan></text>
      <text x="4" y="130" font-family="Questrial, sans-serif" font-size="40" fill="var(--subtitle-ink)">{</text>
      <text x="504" y="130" font-family="Questrial, sans-serif" font-size="40" fill="var(--subtitle-ink)">}</text>
      <text x="30" y="125" textLength="470" lengthAdjust="spacingAndGlyphs"
            font-family="Courgette, cursive" font-size="17" fill="var(--subtitle-ink)">A Simple Guide to Understanding &amp; Controlling Your Blood Sugar</text>
    </g>

    <g fill="none" stroke-linejoin="round">
      <g stroke="#ffffff" stroke-width="96">
        <path d="M358 650 H150 A150 150 0 0 1 0 500 V470 A180 180 0 0 1 180 290 A178 178 0 0 1 358 468 Z"/>
        <path d="M368 650 V568 A82 82 0 0 1 450 486 A82 82 0 0 1 532 568 A82 82 0 0 1 450 650 Z"/>
        <path d="M358 658 V740 A82 82 0 0 1 276 822 A82 82 0 0 1 195 740 A82 82 0 0 1 277 658 Z"/>
        <path d="M368 658 H450 A82 82 0 0 1 532 740 A82 82 0 0 1 450 822 A82 82 0 0 1 368 740 Z"/>
      </g>
      <g stroke="var(--frame-grey)" stroke-width="52">
        <path d="M358 650 H150 A150 150 0 0 1 0 500 V470 A180 180 0 0 1 180 290 A178 178 0 0 1 358 468 Z"/>
        <path d="M368 650 V568 A82 82 0 0 1 450 486 A82 82 0 0 1 532 568 A82 82 0 0 1 450 650 Z"/>
        <path d="M358 658 V740 A82 82 0 0 1 276 822 A82 82 0 0 1 195 740 A82 82 0 0 1 277 658 Z"/>
        <path d="M368 658 H450 A82 82 0 0 1 532 740 A82 82 0 0 1 450 822 A82 82 0 0 1 368 740 Z"/>
      </g>
    </g>

    <g role="img" aria-label="Photo placeholder: a smiling mature couple embracing outdoors in soft daylight">
      <path fill="url(#photo-tone)" d="M358 650 H150 A150 150 0 0 1 0 500 V470 A180 180 0 0 1 180 290 A178 178 0 0 1 358 468 Z"/>
    </g>
    <path fill="var(--petal-green)" d="M368 650 V568 A82 82 0 0 1 450 486 A82 82 0 0 1 532 568 A82 82 0 0 1 450 650 Z"/>
    <path fill="var(--petal-teal)" d="M358 658 V740 A82 82 0 0 1 276 822 A82 82 0 0 1 195 740 A82 82 0 0 1 277 658 Z"/>
    <path fill="var(--petal-pink)" d="M368 658 H450 A82 82 0 0 1 532 740 A82 82 0 0 1 450 822 A82 82 0 0 1 368 740 Z"/>

    <g class="petal-words" font-family="Montserrat, sans-serif" font-weight="700" fill="var(--frame-grey)" letter-spacing="-1.5">
      <text x="378" y="590" textLength="150" lengthAdjust="spacingAndGlyphs" font-size="44">inspire</text>
      <text x="202" y="753" textLength="152" lengthAdjust="spacingAndGlyphs" font-size="50">equip</text>
      <text x="376" y="745" textLength="146" lengthAdjust="spacingAndGlyphs" font-size="31">succeed</text>
    </g>
  </svg>

  <div class="series-mark">
    <span class="series-mark__dot"></span>
    <span>Vital Spark</span>
  </div>
</section>

</body>
</html>
```